Video production company website

VistaKeel Productions is a video and photography production company serving many Fortune 500 clients traveling to Hawaii and International Destinations. Our primary focus is the Corporate and Incentive group market, and offer both photography and video services. In addition, we also create custom marketing, sales, art, and real estate productions.

Target Market(s)

Corporate Incentive Travel Groups

Industry/Entity Type

Videography

Number of Pages Required

4 page

Requirements
Must have
• see doc with content. This will ultimately be needed to be a wordpress design so we can update ourselves.
Nice to have
• sleek design, professional, cutting edge, modern
Should not have
• too much Hawaii Feel, some ok but we do travel international

```html
<!DOCTYPE html>
<html lang="en">
<head>
<meta charset="utf-8">
<title>VistaKeel Productions</title>
<link rel="stylesheet" href="https://fonts.googleapis.com/css2?family=Libre+Baskerville:wght@400;700&family=Open+Sans:wght@400;600;700&display=swap">
<style>
:root{
  --blue:#3b8dcb;
  --navy:#1d4f7c;
  --gold:#c9a24a;
  --ink:#222;
  --muted:#666;
  --light:#f1f1f1;
  --night:#0b0f18;
  --white:#fff;
  --serif:'Libre Baskerville', Georgia, serif;
  --sans:'Open Sans', Arial, sans-serif;
}
*{box-sizing:border-box;margin:0;padding:0}
html,body{width:1200px;height:3346px;overflow:hidden}
body{position:relative;font-family:var(--sans);color:var(--ink);background:var(--white)}
.abs{position:absolute}
.ph{position:absolute}
.section-title{position:absolute;left:0;width:100%;text-align:center;font-family:var(--serif);font-size:17px;letter-spacing:1px;color:var(--navy);text-transform:uppercase;font-weight:700}
.divider{position:absolute;height:14px}
.divider::before{content:"";position:absolute;left:0;right:0;top:6px;height:1px;background:var(--blue)}
.divider span{position:absolute;left:50%;top:0;width:20px;height:14px;margin-left:-10px;border:2px solid var(--gold);border-radius:3px;background:inherit}
.btn{position:absolute;display:flex;align-items:center;justify-content:center;font-size:13px;font-weight:600}
.btn-outline{border:2px solid var(--blue);color:var(--blue);background:var(--white)}
.btn-solid{background:var(--blue);color:var(--white)}

/* hero */
.hero{left:0;top:0;width:1200px;height:462px;background:radial-gradient(circle at 520px 110px,#7a6a58 0,#2b2a33 22%,#0c0f1a 55%),#0c0f1a}
.hero-photo{left:600px;top:60px;width:600px;height:402px;background:linear-gradient(100deg,rgba(40,40,48,0) 0,#3b3a40 30%,#c9b2a0 60%,#6b6464 100%);opacity:.85}
.brand{left:96px;top:26px;display:flex;align-items:center;gap:10px;color:var(--white);font-family:var(--sans);font-weight:700;font-size:17px}
.brand i{width:16px;height:16px;border-radius:50%;background:var(--blue);display:block}
.nav{left:575px;top:30px;display:flex;gap:42px;font-size:13px;font-weight:700;color:var(--white)}
.hero-frame{left:150px;top:170px;width:370px;height:190px;border:2px solid var(--gold);transform:rotate(-15deg);padding:32px 36px;color:var(--white)}
.hero-frame .kicker{font-size:22px;font-weight:700}
.hero-frame .title{font-family:var(--serif);font-size:30px;color:#5aa8e8;letter-spacing:1px}
.hero-frame p{font-size:14px;line-height:1.4;margin-top:10px;color:#e6e6e6}
.dots{left:588px;top:440px;display:flex;gap:8px}
.dots i{width:8px;height:8px;border-radius:50%;background:#777;display:block}
.dots i.on{background:var(--white)}

/* welcome */
.welcome-text{left:190px;top:578px;width:825px;text-align:center;font-size:12.5px;line-height:20px;color:var(--muted)}

/* focus */
.focus{left:0;top:692px;width:1200px;height:356px;background:linear-gradient(180deg,#0f2f52 0,#1a4a78 45%,#152f4a 75%,#2a2d33 100%)}
.focus-frame{left:133px;top:741px;width:453px;height:266px;background:var(--blue)}
.focus-photo{left:107px;top:747px;width:468px;height:246px;border:4px solid var(--white);background:linear-gradient(180deg,#9cc1d9 0,#6e8f5c 40%,#3a3a40 70%,#6a4a7a 100%)}
.focus-title{left:629px;top:766px;width:468px;text-align:center;font-family:var(--serif);font-size:18px;color:var(--white)}
.focus-text{left:629px;top:830px;width:468px;text-align:center;font-size:12.5px;line-height:19px;color:#e8eef5}

/* awards */
.awards{left:0;top:1048px;width:1200px;height:458px;background:linear-gradient(180deg,#fbf6ea 0,#f9edd5 60%,#f5d9b5 100%)}
.timeline{left:597px;top:1170px;width:1px;height:310px;background:#bbb}
.node{position:absolute;width:14px;height:14px;border-radius:50%;border:2px solid var(--blue);background:var(--white)}
.node::after{content:"";position:absolute;left:3px;top:3px;width:4px;height:4px;border-radius:50%;background:var(--blue)}
.award-box{position:absolute;border:1px solid #8a8a8a;background:rgba(255,255,255,.55);padding:12px 22px;font-size:12.5px;line-height:19px;color:var(--muted)}
.award-box.left{text-align:right}
.year{position:absolute;background:var(--blue);color:var(--white);font-weight:700;font-size:15px;display:flex;align-items:center;justify-content:center}

/* gallery */
.tabs{left:0;top:1610px;width:1200px;height:24px}
.tab{position:absolute;font-size:12px;color:#333}
.tab.on::after{content:"";position:absolute;left:-6px;right:-14px;bottom:-8px;height:2px;background:var(--blue)}
.tabline{left:432px;top:1634px;width:335px;height:1px;background:#ddd}
.shot{position:absolute}

/* newsletter & contact */
.newsletter{left:0;top:2338px;width:598px;height:310px;background:linear-gradient(135deg,#3b3a3a 0,#26292f 50%,#1b1d22 100%)}
.contact{left:598px;top:2338px;width:602px;height:310px;background:linear-gradient(135deg,#e9e7e0 0,#dcdad2 100%)}
.nl-title{left:0;top:2408px;width:598px;text-align:center;font-family:var(--serif);font-size:16px;color:var(--white)}
.ct-title{left:598px;top:2408px;width:506px;text-align:center;font-family:var(--serif);font-size:16px;color:var(--navy)}
.field{position:absolute;background:rgba(150,150,150,.55);color:#333;font-size:11px;display:flex;align-items:center;padding-left:30px}
.field::before{content:"";position:absolute;left:10px;top:50%;width:10px;height:10px;margin-top:-5px;background:#555;border-radius:2px}
.nl-input{left:145px;top:2507px;width:401px;height:38px;background:rgba(140,140,140,.35);color:#ddd;font-size:12px;display:flex;align-items:center;justify-content:center}

/* clients & posts */
.clients{left:0;top:2648px;width:1200px;height:452px;background:var(--light)}
.sub-title{position:absolute;font-family:var(--serif);font-size:16px;color:var(--ink);text-align:center}
.client-frame{left:106px;top:2752px;width:232px;height:312px;background:var(--blue)}
.client-photo{left:98px;top:2744px;width:232px;height:312px;border:3px solid var(--white);background:linear-gradient(160deg,#d9dde0 0,#b9c6cf 40%,#6a8aa5 100%)}
.quote-head{left:357px;top:2742px;width:330px;font-weight:700;font-size:15px;line-height:20px;color:var(--ink)}
.quote-text{left:357px;top:2804px;width:330px;font-size:12px;line-height:19px;color:var(--muted)}
.quote-name{left:357px;top:2922px;font-size:12px;color:var(--ink)}
.social{display:flex;gap:6px}
.social i{width:25px;height:25px;display:block;border-radius:2px}
.s1{background:#35a9e0}.s2{background:#d73d32}.s3{background:#3b5998}.s4{background:#0e76a8}
.arrows{left:362px;top:3036px;display:flex;gap:4px}
.arrows span{width:18px;height:18px;border:1px solid #bbb;border-radius:50%;font-size:11px;color:#777;display:flex;align-items:center;justify-content:center}
.vline{left:729px;top:2700px;width:1px;height:316px;background:#ccc}
.post{position:absolute;left:785px;width:318px;height:70px}
.post-thumb{position:absolute;left:0;top:0;width:58px;height:66px;border:2px solid var(--white)}
.post-title{position:absolute;left:86px;top:2px;width:232px;font-weight:700;font-size:11.5px;line-height:16px}
.post-meta{position:absolute;left:86px;top:42px;width:232px;font-size:11px;color:#555;display:flex;justify-content:space-between}
.post-meta b{font-weight:400;display:flex;align-items:center;gap:6px}
.post-meta b::before{content:"";width:10px;height:10px;background:var(--blue);display:block}
.post-sep{position:absolute;left:870px;width:232px;height:1px;background:#d5d5d5}

/* footer */
.footer{left:0;top:3100px;width:1200px;height:246px;background:#000}
.f-title{position:absolute;font-family:var(--serif);font-size:15px;color:var(--blue)}
.f-text{position:absolute;font-size:10.5px;line-height:15px;color:#aaa}
.f-post{position:absolute;left:529px;width:265px;font-size:10.5px;line-height:14px;color:#aaa;font-style:italic;padding-bottom:6px;border-bottom:1px solid #333}
.insta{left:872px;top:3154px;display:grid;grid-template-columns:repeat(5,44px);gap:5px}
.insta i{display:block;width:44px;height:44px;background:linear-gradient(135deg,#6b5a4a,#2e2a2a)}
.copy{left:0;top:3316px;width:1200px;text-align:center;font-size:10.5px;color:#888}
</style>
</head>
<body>

<!-- Hero -->
<header class="hero abs">
  <div class="hero-photo ph" role="img" aria-label="Night fireworks over a resort with a photographer holding a camera"></div>
  <div class="brand abs"><i></i>VistaKeel Productions</div>
  <nav class="nav abs"><span>HOME</span><span>ABOUT</span><span>AWARDS</span><span>GALLARY</span><span>BLOG</span><span>CONTACT US</span></nav>
  <div class="hero-frame abs">
    <div class="kicker">Your fantastic</div>
    <div class="title">MOMENT SHOT</div>
    <p>Lorem Ipsum is simply dummy text of the printing and typesetting industry.</p>
  </div>
  <div class="dots abs"><i></i><i class="on"></i><i></i></div>
</header>

<!-- Welcome -->
<section>
  <h2 class="section-title" style="top:512px">Welcome</h2>
  <div class="divider" style="left:440px;top:537px;width:320px;background:var(--white)"><span></span></div>
  <p class="welcome-text abs">when an unknown printer took a galley of type and scrambled it to make a type specimen book.when an unknown printer took a galley of type and scrambled it to make a type specimen book. It has survived not only five centuries, but also the leap into electronic typesetting It has survived not only five centuries, but also the leap into electronic typesetting</p>
</section>

<!-- Primary focus -->
<section class="focus abs" role="img" aria-label="Dusk cityscape behind a rocky shoreline"></section>
<div class="focus-frame abs"></div>
<div class="focus-photo ph" role="img" aria-label="Large corporate group posing together by a lake"></div>
<h2 class="focus-title abs">OUR PRIMARY FOCUS</h2>
<div class="divider" style="left:698px;top:795px;width:330px;background:#1a4a78"><span></span></div>
<p class="focus-text abs">when an unknown printer took a galley of type and scrambled it to make a type specimen book when an unknown printer took a galley of type and scrambled it to make a type specimen book. It has survived not only five centuries, but also the leap into electronic typesetting It has survived not only five centuries, but also the leap into electronic typesetting</p>
<div class="btn btn-outline" style="left:787px;top:955px;width:145px;height:33px;border-color:var(--white)">Read more</div>

<!-- Awards -->
<section class="awards abs" role="img" aria-label="Soft palm tree silhouette at sunset"></section>
<h2 class="section-title" style="top:1101px">Awards</h2>
<div class="divider" style="left:440px;top:1126px;width:320px;background:#fbf6ea"><span></span></div>
<div class="timeline abs"></div>
<div class="award-box left" style="left:98px;top:1164px;width:471px;height:98px">Contrary to popular belief, Lorem Ipsum is not simplymdom text. It has roots in a piece of classical Latin literature from 45 BC, making it over 2000 years.</div>
<div class="node" style="left:591px;top:1204px"></div>
<div class="year" style="left:622px;top:1193px;width:138px;height:36px">2014</div>
<div class="year" style="left:437px;top:1307px;width:138px;height:34px">2015</div>
<div class="node" style="left:591px;top:1317px"></div>
<div class="award-box" style="left:629px;top:1280px;width:475px;height:94px">Contrary to popular belief, Lorem Ipsum is not simplymdom text. It has roots in a piece of classical Latin literature from 45 BC, making it over 2000 years</div>
<div class="award-box left" style="left:98px;top:1378px;width:471px;height:96px">Contrary to popular belief, Lorem Ipsum is not simplymdom text. It has roots in a piece of classical Latin literature from 45 BC, making it over 2000 years</div>
<div class="node" style="left:591px;top:1415px"></div>
<div class="year" style="left:622px;top:1405px;width:138px;height:34px">2016</div>

<!-- Gallery -->
<h2 class="section-title" style="top:1549px">Gallery</h2>
<div class="divider" style="left:440px;top:1574px;width:320px;background:var(--white)"><span></span></div>
<div class="tabline abs"></div>
<div class="tabs abs">
  <span class="tab on" style="left:440px;top:0">All</span>
  <span class="tab" style="left:512px;top:0">Images</span>
  <span class="tab" style="left:616px;top:0">Video</span>
  <span class="tab" style="left:708px;top:0">Category</span>
</div>
<div class="shot" role="img" aria-label="Outdoor dinner party at sunset" style="left:98px;top:1662px;width:281px;height:363px;background:linear-gradient(180deg,#c69a6e 0,#5b5a6a 35%,#3b5a6a 70%,#d9d9d9 100%)"></div>
<div class="shot" role="img" aria-label="Man jumping into turquoise sea" style="left:98px;top:2045px;width:281px;height:177px;background:linear-gradient(180deg,#46b6c8,#1e8aa2)"></div>
<div class="shot" role="img" aria-label="Fireworks over a crowd at night" style="left:399px;top:1666px;width:402px;height:266px;background:radial-gradient(circle at 50% 35%,#8a7a6a 0,#1a1a22 45%,#0a0a10 100%)"></div>
<div class="shot" role="img" aria-label="Group in floral dresses at a garden party" style="left:399px;top:1954px;width:402px;height:268px;background:linear-gradient(180deg,#2e3b2a,#1c2630)"></div>
<div class="abs" style="left:413px;top:1968px;width:374px;height:240px;border:1px solid var(--blue)"></div>
<div class="abs" style="left:588px;top:2072px;width:18px;height:18px;border:2px solid var(--white);border-radius:50%"></div>
<div class="shot" role="img" aria-label="Dancers performing in pink stage light" style="left:823px;top:1668px;width:281px;height:183px;background:linear-gradient(135deg,#c21f7a,#e8558a 50%,#7a1a3a)"></div>
<div class="shot" role="img" aria-label="Golfer mid swing on a course" style="left:823px;top:1871px;width:281px;height:351px;background:linear-gradient(180deg,#a8c4d8 0,#7b9a7a 50%,#5a6e4a 100%)"></div>
<div class="btn btn-outline" style="left:526px;top:2259px;width:145px;height:34px">View all</div>

<!-- Newsletter & contact -->
<section class="newsletter abs" role="img" aria-label="Creative desk with laptop and notebooks"></section>
<section class="contact abs" role="img" aria-label="City street map"></section>
<h3 class="nl-title abs">Subscribe our newsletter</h3>
<div class="divider" style="left:172px;top:2432px;width:330px;background:#2e3035"><span></span></div>
<div class="nl-input abs">Enter your email id</div>
<div class="btn btn-solid" style="left:272px;top:2597px;width:145px;height:33px">Submit</div>
<h3 class="ct-title abs">Contact us</h3>
<div class="divider" style="left:685px;top:2432px;width:332px;background:#e2e0d9"><span></span></div>
<div class="field" style="left:685px;top:2465px;width:332px;height:25px">Name*</div>
<div class="field" style="left:685px;top:2500px;width:332px;height:27px">Email*</div>
<div class="field" style="left:685px;top:2536px;width:332px;height:45px;align-items:flex-start;padding-top:6px">Message*</div>
<div class="btn btn-solid" style="left:778px;top:2597px;width:145px;height:33px">Send</div>

<!-- Clients & posts -->
<section class="clients abs"></section>
<h3 class="sub-title" style="left:228px;top:2684px;width:316px">Our Clients Says</h3>
<div class="divider" style="left:228px;top:2708px;width:316px;background:var(--light)"><span></span></div>
<div class="client-frame abs"></div>
<div class="client-photo ph" role="img" aria-label="Portrait of a smiling client"></div>
<h4 class="quote-head abs">Cras dictum orci vitae velit vehiula, ac lobo rtis ante luctus.</h4>
<p class="quote-text abs">Praesent vel nunc in felis hendrerit consectetur sed ege stas justo. Vivamus facilisis pretium iaculis. Nulla phar etra tincidunt nibh sit amet mattis. Quisque molestie tinc at justo feugiat, vel tincidunt massa lobortis. Maecenas l aoreet tempor lorem, vitae tempus mi mattis sed.</p>
<div class="quote-name abs">- Oliva Mcman</div>
<div class="social abs" style="left:357px;top:2960px"><i class="s1"></i><i class="s2"></i><i class="s3"></i><i class="s4"></i></div>
<div class="arrows abs"><span>‹</span><span>›</span></div>
<div class="vline abs"></div>
<h3 class="sub-title" style="left:785px;top:2684px;width:322px">Latest Posts</h3>
<div class="divider" style="left:785px;top:2708px;width:322px;background:var(--light)"><span></span></div>
<div class="post" style="top:2744px">
  <div class="post-thumb" role="img" aria-label="Author portrait" style="background:linear-gradient(135deg,#555,#222)"></div>
  <div class="post-title">Lorem Ipsum is simply Dummy Text. Nolla pharetra ti..</div>
  <div class="post-meta"><span>- Tomy Deo</span><b>28/01/16</b></div>
</div>
<div class="post-sep" style="top:2820px"></div>
<div class="post" style="top:2833px">
  <div class="post-thumb" role="img" aria-label="Author portrait" style="background:linear-gradient(135deg,#c2643a,#7a3a22)"></div>
  <div class="post-title">Lorem Ipsum is simply Dummy Text. Nolla pharetra ti..</div>
  <div class="post-meta"><span>- July fox</span><b>21/01/16</b></div>
</div>
<div class="post-sep" style="top:2909px"></div>
<div class="post" style="top:2922px">
  <div class="post-thumb" role="img" aria-label="Author portrait" style="background:linear-gradient(135deg,#999,#444)"></div>
  <div class="post-title">Lorem Ipsum is simply Dummy Text. Nolla pharetra ti..</div>
  <div class="post-meta"><span>- Alisha Jo</span><b>28/01/16</b></div>
</div>

<!-- Footer -->
<footer class="footer abs"></footer>
<h4 class="f-title" style="left:100px;top:3124px">About Us</h4>
<p class="f-text" style="left:100px;top:3158px;width:320px">Lorem ipsum dolor sit amet, consectetur adipiscing elit. Inte ger vehicula sollicitudin magna sed viverra. Curabitur id enim ac ante rutrum tempus nec quis massa. Morbi dictum quis turpis id consectetur. Phasellus maximus dui at neque facilisis, ut porttitor sapien semper</p>
<div class="social abs" style="left:100px;top:3268px"><i class="s1"></i><i class="s2"></i><i class="s3"></i><i class="s4"></i></div>
<h4 class="f-title" style="left:529px;top:3124px">Latest Posts</h4>
<p class="f-post" style="top:3152px">"Neque porro quisquam est qui dolorem ipsum quia dolor sit amet, consectetur, adipisci velit..."</p>
<p class="f-post" style="top:3200px">"Neque porro quisquam est qui dolorem ipsum quia dolor sit amet, consectetur, adipisci velit..."</p>
<p class="f-post" style="top:3248px">"Neque porro quisquam est qui dolorem ipsum quia dolor sit amet, consectetur, adipisci velit..."</p>
<h4 class="f-title" style="left:872px;top:3124px">Instagram</h4>
<div class="insta abs" role="img" aria-label="Grid of event photos">
  <i></i><i></i><i></i><i></i><i></i>
  <i></i><i></i><i></i><i></i><i></i>
  <i></i><i></i>
</div>
<div class="copy abs">Copy right © 2016</div>

</body>
</html>
```